Window Graphics ‘Opening Soon’ for new Jewellery Boutique

We want to fully cover the shop window for a duration of 6 weeks whilst the refurbishment is going on. The window graphics should be cool, sexy and sophisticated. The graphics should include our company logo ‘THE COPPER LANTERN’ in Gills Sans Font. The shop will be an upmarket jewellery watch shop.

Target Market(s)

Jewellery customers

Industry/Entity Type

Jewellery

Colors

Designer to choose colors to be used in the design.

Requirements
Must have
• Must be loud graphics that catch your attention when walking past. I have provided a graphics example where the colour palette is black, white and shocking pink!
Nice to have
• The Boss is Back…. The Copper Lantern Proudly present a new masterpiece coming soon….

```html
<!DOCTYPE html>
<html lang="en">
<head>
<meta charset="utf-8">
<title>Front Elevation – Window Graphics</title>
<link href="https://fonts.googleapis.com/css2?family=Montserrat:wght@700;800&family=Lato:wght@400;700&family=Arimo&display=swap" rel="stylesheet">
<style>
  :root {
    --paper: #ffffff;
    --ink: #000000;
    --frame-grey: #6e6e6e;
    --shock-pink: #e9338f;
    --cream: #f7eed3;
    --dim-red: #c8423c;
  }
  html, body { margin: 0; padding: 0; overflow: hidden; background: var(--paper); }
  .sheet { position: relative; width: 1200px; height: 851px; overflow: hidden; background: var(--paper); font-family: "Lato", sans-serif; color: var(--ink); }
  .elevation { position: absolute; left: 0; top: 0; }
  .display-type { font-family: "Montserrat", sans-serif; font-weight: 800; }
  .dim-label { font-family: "Arimo", sans-serif; font-size: 25px; fill: var(--ink); }
  .sheet-title { font-family: "Lato", sans-serif; font-size: 15px; fill: var(--ink); }

  .title-block { position: absolute; left: 1022px; width: 119px; box-sizing: border-box; border: 1.6px solid var(--frame-grey); font-size: 6.4px; line-height: 1.3; }
  .title-block .label { font-weight: 700; }
  .general-notes { top: 79px; height: 305px; padding: 12px 10px 6px 4px; }
  .general-notes ol { margin: 0; padding-left: 12px; font-size: 5.6px; line-height: 1.22; text-align: justify; }
  .project { top: 395px; height: 35px; padding: 4px 6px; }
  .project .value { margin: 3px 0 0 30px; }
  .address { top: 440px; height: 59px; padding: 4px 6px; }
  .address .value { text-align: center; margin-top: 9px; line-height: 1.2; }
  .drawing-title { top: 509px; height: 33px; padding: 4px 6px; }
  .drawing-title .value { margin: 1px 0 0 28px; }
  .date { top: 547px; height: 19px; padding: 4px 6px; }
  .ref { top: 573px; height: 18px; padding: 4px 6px; width: 77px; }
  .rev { top: 573px; left: 1099px; height: 18px; padding: 4px 6px; width: 42px; }
  .scale { top: 595px; height: 33px; padding: 4px 6px; }
  .scale .value { position: absolute; left: 56px; top: 3px; }
  .studio { top: 638px; height: 171px; padding: 20px 6px; text-align: center; }
  .studio .name { margin-bottom: 8px; }
  .studio .chair-art { width: 56px; height: 76px; margin: 18px auto 0; background: linear-gradient(160deg, #d9d9d9, #8a8a8a); border-radius: 4px; }
</style>
</head>
<body>
<div class="sheet">
  <svg class="elevation" width="1200" height="851" viewBox="0 0 1200 851" aria-label="Front elevation of shop window graphics">
    <defs>
      <clipPath id="window-panels">
        <rect x="138" y="387" width="141" height="331"/>
        <rect x="292" y="387" width="508" height="331"/>
        <rect x="814" y="387" width="134" height="331"/>
      </clipPath>
    </defs>

    <rect x="56" y="67" width="1094" height="752" fill="none" stroke="var(--frame-grey)" stroke-width="1.8"/>
    <line x1="1014" y1="67" x2="1014" y2="819" stroke="var(--frame-grey)" stroke-width="1.8"/>
    <text class="sheet-title" x="70" y="96">FRONT ELEVATION</text>

    <g class="dimensions" stroke="var(--dim-red)" stroke-width="0.8" fill="none">
      <line x1="130" y1="191" x2="955" y2="191"/>
      <path d="M127 194 L133 188 M952 194 L958 188"/>
      <line x1="94" y1="227" x2="94" y2="725"/>
      <path d="M91 224 L97 230 M91 376 L97 382 M91 722 L97 728"/>
      <line x1="995" y1="227" x2="995" y2="725"/>
      <path d="M992 224 L998 230 M992 722 L998 728"/>
    </g>
    <rect x="512" y="178" width="60" height="26" fill="var(--paper)"/>
    <text class="dim-label" x="542" y="200" text-anchor="middle">5530</text>
    <rect x="82" y="275" width="24" height="58" fill="var(--paper)"/>
    <text class="dim-label" transform="translate(103 303) rotate(-90)" text-anchor="middle">1020</text>
    <rect x="82" y="524" width="24" height="58" fill="var(--paper)"/>
    <text class="dim-label" transform="translate(103 553) rotate(-90)" text-anchor="middle">2320</text>
    <rect x="983" y="446" width="24" height="58" fill="var(--paper)"/>
    <text class="dim-label" transform="translate(1004 476) rotate(-90)" text-anchor="middle">3350</text>

    <g class="fascia" stroke="var(--ink)" stroke-width="1.2" fill="none">
      <rect x="131" y="227" width="823" height="152"/>
      <line x1="131" y1="246.2" x2="954" y2="246.2"/>
      <line x1="131" y1="265.5" x2="954" y2="265.5"/>
      <line x1="131" y1="284.7" x2="954" y2="284.7"/>
      <line x1="131" y1="304" x2="954" y2="304"/>
      <line x1="131" y1="323.2" x2="954" y2="323.2"/>
      <line x1="131" y1="342.5" x2="954" y2="342.5"/>
      <line x1="131" y1="361.7" x2="954" y2="361.7"/>
    </g>

    <g class="window-frame" stroke="var(--ink)" stroke-width="1.2" fill="none">
      <rect x="131" y="379" width="823" height="346"/>
      <line x1="286" y1="379" x2="286" y2="725"/>
      <line x1="807" y1="379" x2="807" y2="725"/>
    </g>

    <g class="window-graphics" clip-path="url(#window-panels)">
      <rect x="130" y="380" width="830" height="345" fill="var(--shock-pink)"/>
      <text class="display-type" x="138" y="449" font-size="82" fill="var(--ink)" textLength="141" lengthAdjust="spacingAndGlyphs">THE</text>
      <text class="display-type" x="292" y="579" font-size="266" fill="var(--ink)" textLength="656" lengthAdjust="spacingAndGlyphs">BOSS</text>
      <text class="display-type" x="140" y="730" font-size="200" fill="var(--ink)" textLength="139" lengthAdjust="spacingAndGlyphs">IS</text>
      <text class="display-type" x="292" y="730" font-size="200" fill="var(--paper)" textLength="508" lengthAdjust="spacingAndGlyphs">BACK</text>
      <text class="display-type" x="817" y="628" font-size="18" fill="var(--cream)" textLength="129" lengthAdjust="spacingAndGlyphs">A MASTERPIECE</text>
      <text class="display-type" x="816" y="656" font-size="35" fill="var(--cream)" textLength="130" lengthAdjust="spacingAndGlyphs">COMING</text>
      <text class="display-type" x="816" y="690" font-size="42" fill="var(--cream)" textLength="128" lengthAdjust="spacingAndGlyphs">SOON</text>
      <path class="door-pull" d="M814 520 A33 33 0 0 1 814 585" fill="none" stroke="var(--ink)" stroke-width="6"/>
      <path d="M814 520 A33 33 0 0 1 814 585" fill="none" stroke="var(--paper)" stroke-width="3.6"/>
    </g>

    <g class="brand-name">
      <text class="display-type" x="209" y="545" font-size="11" fill="var(--paper)" text-anchor="middle" textLength="116" lengthAdjust="spacingAndGlyphs">THE COPPER LANTERN</text>
    </g>
  </svg>

  <div class="title-block general-notes">
    <ol>
      <li>THE DRAWING SHOWS DESIGN INTENT ONLY. ALL DIMENSIONS TO BE CHECKED ON SITE PRIOR TO CONSTRUCTION OR PRODUCTION. CONSTRUCTION DETAILS TO BE CONFIRMED BY CONTRACTOR / MANUFACTURER BY SUBMITTING SHOP DRAWINGS FOR DESIGNERS APPROVAL.</li>
      <li>DESIGN / DRAWING IS NOT TO BE SCALED FOR PRODUCTION AND CONSTRUCTION PURPOSE.</li>
      <li>ALL DISCREPANCIES AND OMISSIONS ON SITE MUST BE REPORTED TO DESIGNER FOR THEIR COMMENTS OR APPROVAL PRIOR TO COMMENCING WORK.</li>
      <li>ALL ELECTRICAL LIGHTING, HVAC AND PLUMBING ISSUES TO BE REFERRED TO ENGINEER'S DRAWINGS PRIOR TO COMMENCEMENT O WORKS.</li>
      <li>THE DESIGNS ARE SUBJECT TO APPROVAL BY STATUTORY AUTHORITIES AND ANY NECESSARY ALTERATIONS SHOULD BE MADE IF REQUIRED TO COMPLY WITH STATUTORY REQUIREMENTS. ALL DESIGN CONCEPTS AND DRAWINGS ARE THE PROPERTY OF THE COPPER LANTERN LONDON AND ARE COVERED BY COPYRIGHT. NO REPRODUCTIONS, ADAPTATIONS AND/OR COPIES MAY BE MADE WITHOUT WRITTEN PERMISSION BY THE COPPER LANTERN LONDON.</li>
    </ol>
  </div>
  <div class="title-block project"><div class="label">PROJECT:</div><div class="value">VESTA LONDON</div></div>
  <div class="title-block address"><div class="label">ADDRESS:</div><div class="value">14 ALDER ROW<br>MARLOWE YARD<br>LONDON<br>EC9 4QT</div></div>
  <div class="title-block drawing-title"><div class="label">TITLE:</div><div class="value">FRONT ELEVATION</div></div>
  <div class="title-block date"><span class="label">DATE:</span>&nbsp; 28 / 09 / 2021</div>
  <div class="title-block ref"><span class="label">REF. NO:</span> MG</div>
  <div class="title-block rev"><span class="label">REV:</span> A</div>
  <div class="title-block scale"><span class="label">SCALE:</span><span class="value">NTS</span></div>
  <div class="title-block studio">
    <div class="name">THE COPPER LANTERN</div>
    <div>8 Finch Lane, Harwick,<br>London WC9 2ZP</div>
    <div class="chair-art" role="img" aria-label="Ink sketch of an upholstered armchair"></div>
  </div>
</div>
</body>
</html>
```